Innovative approaches to treat addiction

PowerPoint on different techniques
Add graphics to screen
Easy to follow
I've provided the PowerPoint w content
Now make it pretty
And
hand outs for them to follow and take notes
Can you also add my bio:
Mara J. Trevanion, MS LCADC is a licensed Psychotherapist with a specialty in Addiction Disorders and over 22 years of clinical experience. Her integrative approach to counseling combines years of clinical experience with cognitive behavioral and traditional psychotherapy, with holistic therapies including; mindfulness, NLP, hypnotherapy, yoga therapy, reiki, motivational and wellness coaching.
Handout materials for them to follow and take notes

```html
<!DOCTYPE html>
<html lang="en">
<head>
<meta charset="utf-8">
<title>Innovative Techniques to Treat Disorders – Slide Deck</title>
<link href="https://fonts.googleapis.com/css2?family=Arimo:ital,wght@0,400;0,700;1,400&display=swap" rel="stylesheet">
<style>
  :root{
    --stage:#1d2352;
    --blue-deep:#0b3a80;
    --blue-mid:#1a5cad;
    --blue-light:#3d86d2;
    --footer:#1a4d94;
    --footer-text:#a9c6ea;
    --white:#ffffff;
    --ink:#1b1b1b;
    --oval-top:#eef6fb;
    --oval-bottom:#bcd8e6;
    --oval-text:#1c5b9a;
    --table-head:#1d4f97;
    --table-body:#dbe9f3;
    --line:#333a44;
  }
  *{margin:0;padding:0;box-sizing:border-box}
  html,body{width:1200px;height:918px;overflow:hidden;background:var(--stage)}
  body{position:relative;font-family:"Arimo",Arial,sans-serif;color:var(--ink)}

  .slide{position:absolute;width:531px;height:398px;background:var(--white);overflow:hidden;box-shadow:0 2px 10px rgba(0,0,0,.35)}
  .slide--title{left:53px;top:38px;background:radial-gradient(ellipse at 65% 60%,var(--blue-light) 0%,var(--blue-mid) 40%,var(--blue-deep) 100%)}
  .slide--bio{left:618px;top:38px}
  .slide--results{left:53px;top:469px}
  .slide--mindful{left:618px;top:469px}

  .slide-header{position:absolute;left:0;top:0;width:100%;height:92px;
    background:linear-gradient(180deg,var(--blue-deep) 0%,var(--blue-mid) 70%,#2f74c4 100%)}
  .header-icon{position:absolute;left:22px;top:6px;width:78px;height:84px;border-radius:40px 40px 10px 10px;
    background:radial-gradient(circle at 45% 40%,rgba(255,255,255,.45),rgba(255,255,255,.08) 70%)}
  .slide-title{position:absolute;color:var(--white);font-weight:400}

  .slide-footer{position:absolute;left:0;bottom:0;width:100%;height:19px;background:var(--footer);
    display:flex;align-items:center;justify-content:space-between;padding:0 8px 0 32px;font-size:9px;color:var(--footer-text)}

  /* Title slide */
  .hero-art{position:absolute;left:300px;top:40px;width:200px;height:330px;border-radius:110px 110px 20px 20px;
    background:radial-gradient(ellipse at 45% 40%,rgba(255,255,255,.35),rgba(255,255,255,.05) 70%)}
  .title-band{position:absolute;left:0;top:196px;width:400px;height:92px;
    background:linear-gradient(90deg,var(--white) 0%,var(--white) 80%,rgba(255,255,255,0) 100%);
    text-align:center;padding-top:6px}
  .title-band h1{font-weight:400;font-size:22px;line-height:29px;color:#111;width:330px}
  .title-band p{font-size:14px;margin-top:6px;width:330px}
  .title-footer{position:absolute;right:8px;bottom:3px;font-size:9px;color:var(--footer-text)}

  /* Bio slide */
  .bio-text{position:absolute;left:26px;top:136px;width:315px;font-style:italic;font-size:13px;line-height:24px}
  .bio-photo{position:absolute;left:349px;top:149px;width:167px;height:168px;
    background:linear-gradient(160deg,#8a6b5c 0%,#5a3f36 45%,#1d1414 100%)}

  /* Results slide */
  .diagram{position:absolute;left:0;top:92px;width:531px;height:240px}
  .hub{position:absolute;left:229px;top:110px;width:72px;height:90px;border-radius:36px 36px 10px 30px;
    background:radial-gradient(circle at 55% 35%,#c86aa8 0%,#6b57b9 30%,#111 62%)}
  .node{position:absolute;width:118px;height:45px;border-radius:50%;
    background:linear-gradient(180deg,var(--oval-top),var(--oval-bottom));box-shadow:0 2px 3px rgba(0,0,0,.25);
    display:flex;align-items:center;justify-content:center;text-align:center;
    color:var(--oval-text);font-size:13px;line-height:16px}
  .tagline{position:absolute;left:0;width:100%;top:322px;text-align:center;color:var(--blue-mid);font-size:19px}
  .note{position:absolute;left:44px;top:357px;width:470px;font-size:8px;line-height:10px;font-style:italic}

  /* Mindfulness slide */
  .stones-art{position:absolute;left:394px;top:8px;width:122px;height:84px;
    background:radial-gradient(ellipse at 50% 55%,#4a4f57 0%,#1e2127 55%,rgba(30,33,39,0) 72%)}
  .definition{position:absolute;left:25px;top:108px;width:490px;font-style:italic;font-size:16.5px;line-height:19px}
  .benefits{position:absolute;left:25px;top:151px;width:495px;font-size:12.5px;list-style:none}
  .benefits > li::before{content:"•";position:absolute;left:0}
  .benefits > li{padding-left:20px}
  .benefits ul{list-style:none;margin-top:3px;padding-left:8px;font-size:11px;line-height:16px}
  .benefits ul li::before{content:"–";margin-right:10px}
  .study{position:absolute;left:35px;top:220px;width:477px;height:137px;border-collapse:collapse;font-size:11px;line-height:14px;background:var(--table-body)}
  .study th{background:var(--table-head);color:var(--white);text-align:left;font-size:11.5px;height:19px;padding:0 6px}
  .study td{vertical-align:top;padding:3px 6px}
</style>
</head>
<body>

<section class="slide slide--title">
  <div class="hero-art" role="img" aria-label="Illustration of a head profile with turning gears"></div>
  <div class="title-band">
    <h1>Innovative Techniques<br>to Treat Disorders</h1>
    <p>Mara Trevanion, MS LCADC, CHT, 500RYT</p>
  </div>
  <span class="title-footer">Mara Trevanion</span>
</section>

<section class="slide slide--bio">
  <header class="slide-header">
    <div class="header-icon" role="img" aria-label="Head outline with gears icon"></div>
    <h2 class="slide-title" style="left:112px;top:36px;font-size:26px">Mara J. Trevanion - BIO</h2>
  </header>
  <p class="bio-text">Mara J. Trevanion, MS LCADC is a licensed Psychotherapist with a specialty in Addiction Disorders and over 22 years of clinical experience. Her integrative approach to counseling combines years of clinical experience with cognitive behavioral and traditional psychotherapy, with holistic therapies including; mindfulness, NLP, hypnotherapy, yoga therapy, reiki, motivational and wellness coaching.</p>
  <div class="bio-photo" role="img" aria-label="Portrait photo of the presenter"></div>
  <footer class="slide-footer"><span>8/26/2016</span><span>Innovative Techniques to Treat Disorders</span><span>Mara Trevanion</span></footer>
</section>

<section class="slide slide--results">
  <header class="slide-header">
    <div class="header-icon" role="img" aria-label="Head outline with gears icon"></div>
    <h2 class="slide-title" style="left:109px;top:21px;font-size:16.5px;line-height:22px">Innovative Techniques to Treat Disorders<br>&nbsp;Results of the tools you will learn</h2>
  </header>
  <div class="diagram">
    <svg width="531" height="240" style="position:absolute;left:0;top:0">
      <g stroke="var(--line)" stroke-width="0.8">
        <line x1="266" y1="140" x2="266" y2="54"/>
        <line x1="266" y1="140" x2="146" y2="82"/>
        <line x1="266" y1="140" x2="387" y2="82"/>
        <line x1="266" y1="140" x2="146" y2="164"/>
        <line x1="266" y1="140" x2="387" y2="164"/>
        <line x1="266" y1="140" x2="266" y2="194"/>
      </g>
    </svg>
    <div class="hub" role="img" aria-label="Silhouette of a head with a colourful brain"></div>
    <div class="node" style="left:207px;top:9px">Patient<br>Rapport</div>
    <div class="node" style="left:87px;top:35px">Patient<br>Retention</div>
    <div class="node" style="left:328px;top:35px">Healing<br>Time</div>
    <div class="node" style="left:87px;top:142px">Stress and<br>Burnout</div>
    <div class="node" style="left:328px;top:142px">Treatment<br>Compliance</div>
    <div class="node" style="left:207px;top:172px">Fun &amp;<br>Sustainable</div>
  </div>
  <p class="tagline">Anyone can do it!</p>
  <p class="note">Note: These techniques are not a replacement for standard medical procedures, but work in conjunction with them by freeing the patient of feelings or attitudes that may be compromising his/her natural immune system.</p>
  <footer class="slide-footer"><span>8/26/2016</span><span>Innovative Techniques to Treat Disorders</span><span>Mara Trevanion</span></footer>
</section>

<section class="slide slide--mindful">
  <header class="slide-header">
    <div class="header-icon" role="img" aria-label="Head outline with gears icon"></div>
    <h2 class="slide-title" style="left:125px;top:36px;font-size:26px">Mindfulness</h2>
    <div class="stones-art" role="img" aria-label="Stack of balanced dark stones"></div>
  </header>
  <p class="definition">The practice of being aware of daily experiences with the intention to create a non-judgmental state of awareness.</p>
  <ul class="benefits">
    <li>Benefits:
      <ul>
        <li>Prevents relapse, control cravings, control negative emotions,</li>
        <li>Individuals able to monitor their well-being, recognize discomfort, reduces adrenalin</li>
      </ul>
    </li>
  </ul>
  <table class="study">
    <thead><tr><th style="width:127px">Conducted by</th><th style="width:143px">Research</th><th>Results</th></tr></thead>
    <tbody><tr>
      <td>Helen Marsh, Ph.D.<br>Northgate University, October 2009- July 2012</td>
      <td>Long term effects using mindfulness based treatments.</td>
      <td>Mindfulness practices may support long-term outcomes by strengthening the ability to monitor and skillfully cope with discomfort associated with craving or negative affect.</td>
    </tr></tbody>
  </table>
  <footer class="slide-footer"><span>8/26/2016</span><span>Innovative Techniques to Treat Disorders</span><span>Mara Trevanion</span></footer>
</section>

</body>
</html>
```